Business Card Design Project

We need a buisness card for a new digital sinage company. Our target cliants are small to mediaum buisness who want to advertise on out digital sinage network

Target Market(s)

Small to medium buisness

Industry/Entity Type

Digital

Requirements
Must have
• Must have logo

```html
<!DOCTYPE html>
<html lang="en">
<head>
<meta charset="utf-8">
<title>Vizo Business Card</title>
<link rel="stylesheet" href="https://fonts.googleapis.com/css2?family=Exo+2:wght@400;800&display=swap">
<style>
  :root {
    --page: #ffffff;
    --green-dark: #4e8356;
    --green-light: #b2c595;
    --gold: #d8a95a;
    --gold-light: #dcb866;
    --blue-dark: #4a6c99;
    --blue-light: #7bacbf;
    --ink: #141414;
    --white: #ffffff;
    --shadow: rgba(0, 0, 0, 0.35);
  }
  html, body {
    margin: 0;
    padding: 0;
    width: 1200px;
    height: 1020px;
    overflow: hidden;
    background: var(--page);
    font-family: "Exo 2", Arial, sans-serif;
  }
  .canvas {
    position: relative;
    width: 1200px;
    height: 1020px;
  }
  .card {
    position: absolute;
    width: 608px;
    height: 366px;
    overflow: hidden;
    box-shadow: 0 2px 6px var(--shadow);
  }
  .card-front {
    left: 96px;
    top: 118px;
    background: linear-gradient(100deg, var(--green-light) 10%, var(--green-dark) 92%);
  }
  .front-art {
    position: absolute;
    inset: 0;
    width: 100%;
    height: 100%;
  }
  .brand-mark {
    position: absolute;
    left: 67px;
    top: 58px;
    width: 118px;
    height: 118px;
    background: var(--blue-dark);
  }
  .brand-name {
    position: absolute;
    left: 208px;
    top: 104px;
    margin: 0;
    font-weight: 800;
    font-size: 96px;
    line-height: 1;
    color: var(--ink);
    letter-spacing: -1px;
  }
  .website {
    position: absolute;
    right: 10px;
    bottom: 12px;
    margin: 0;
    font-size: 12px;
    line-height: 1;
    color: var(--white);
    letter-spacing: 0.3px;
  }
  .card-back {
    left: 496px;
    top: 560px;
    background: linear-gradient(90deg, var(--green-dark) 5%, var(--green-light) 95%);
  }
  .info-band {
    position: absolute;
    left: 0;
    top: 63px;
    width: 100%;
    height: 207px;
    background: linear-gradient(90deg, var(--blue-dark), var(--blue-light));
  }
  .gold-rule {
    position: absolute;
    left: 0;
    top: 270px;
    width: 100%;
    height: 12px;
    background: var(--gold-light);
  }
  .person-name {
    position: absolute;
    left: 320px;
    top: 86px;
    margin: 0;
    font-weight: 400;
    font-size: 19px;
    line-height: 24px;
    color: var(--white);
  }
  .contact-list {
    position: absolute;
    left: 70px;
    top: 147px;
    margin: 0;
    padding: 0;
    list-style: none;
    font-size: 17px;
    line-height: 21.6px;
    color: var(--white);
  }
</style>
</head>
<body>
<main class="canvas">
  <section class="card card-front">
    <svg class="front-art" viewBox="0 0 507 304" preserveAspectRatio="none" aria-hidden="true">
      <defs>
        <linearGradient id="sky-swoosh" x1="0" y1="0" x2="1" y2="0">
          <stop offset="0" stop-color="#5ab8e2"/>
          <stop offset="1" stop-color="#2f5ea6"/>
        </linearGradient>
        <linearGradient id="gold-sweep" x1="0" y1="1" x2="1" y2="0">
          <stop offset="0" stop-color="#ddb961"/>
          <stop offset="1" stop-color="#d59d52"/>
        </linearGradient>
      </defs>
      <path d="M0,0 H464 C494,30 494,88 456,128 C392,196 228,262 0,268 Z" fill="url(#gold-sweep)"/>
      <path d="M0,0 H452 C480,32 478,86 440,122 C376,184 216,238 0,242 Z" fill="#ffffff"/>
      <path d="M0,0 H82 C52,10 22,30 0,56 Z" fill="url(#sky-swoosh)"/>
    </svg>
    <span class="brand-mark"></span>
    <p class="brand-name">Vizo</p>
    <p class="website">www.vizomedia.com.au</p>
  </section>

  <section class="card card-back">
    <div class="info-band"></div>
    <div class="gold-rule"></div>
    <h1 class="person-name">Marcus Delaney</h1>
    <ul class="contact-list">
      <li>marcus@vizomedia.com.au</li>
      <li>0400123987</li>
      <li>PO Box 517 Ridgeway WA 6790</li>
    </ul>
  </section>
</main>
</body>
</html>
```